Redesigned PowerPoint template for Restaurant Services Company

We need a redesigned company template for powerpoints. looking for something modern and easy to use. If we like it, we will add additional products for the design (letterhead, social media banners, etc).

Target Market(s)

restaurant owners, and franchise owners

Font styles to use
Serif
Sans Serif

Colors
0355a3
f0474d
ffffff

Requirements
Must have
• - something that uses our colors in a modern way
- easy to use
- something that is eye catching
Nice to have
• - multiple slide types (picture and text, graphic and text, bulleted text, etc)
- easy way to swap out our prospects logo and have our prospects logo displayed throughout the deck
Should not have
• should not have locked or anchored fields making it difficult to edit

```html
<!DOCTYPE html>
<html lang="en">
<head>
<meta charset="utf-8">
<title>Oakvale Execution Network</title>
<link rel="stylesheet" href="https://fonts.googleapis.com/css2?family=Lato:wght@400&family=Oswald:wght@700&display=swap">
<style>
  :root {
    --brand-blue: #0355a3;
    --brand-red: #f0474d;
    --side-teal: #345c72;
    --hub-grey: #dfe2e6;
    --ink: #111111;
    --white: #ffffff;
    --connector: #1f4f86;
  }
  * { margin: 0; padding: 0; box-sizing: border-box; }
  html, body { width: 1200px; height: 675px; overflow: hidden; background: var(--white); }
  .slide {
    position: relative;
    width: 1200px;
    height: 675px;
    overflow: hidden;
    background: var(--white);
    font-family: "Lato", "Gill Sans", sans-serif;
  }
  .top-rule { position: absolute; left: 0; top: 0; width: 1200px; height: 8px; background: var(--brand-blue); }
  .side-strip { position: absolute; left: 0; top: 0; width: 28px; height: 675px; background: var(--side-teal); }
  .footer-band {
    position: absolute; left: 0; bottom: 0; width: 1200px; height: 34px;
    background: var(--brand-blue); color: var(--white); font-size: 13px;
  }
  .footer-band span { position: absolute; top: 9px; }
  .footer-date { left: 131px; }
  .footer-url { left: 0; width: 1228px; text-align: center; }
  .footer-page { left: 1105px; }
  .network-art { position: absolute; left: 0; top: 0; }
  .hub-title {
    position: absolute; left: 337px; top: 190px; width: 540px;
    text-align: center; color: var(--brand-red);
    font-family: "Oswald", "Arial Narrow", sans-serif; font-weight: 700;
    font-size: 62px; line-height: 82px; letter-spacing: 0.28em;
    text-indent: 0.28em;
  }
  .service-box {
    position: absolute; display: flex; align-items: center; justify-content: center;
    background: var(--brand-blue); color: var(--white); text-align: center;
    font-size: 15.5px; line-height: 1.35; border: 1px solid #9fb8d6;
  }
  .box-operations { left: 37px; top: 20px; width: 138px; height: 78px; }
  .box-technology { left: 221px; top: 18px; width: 138px; height: 77px; }
  .box-design { left: 425px; top: 9px; width: 283px; height: 39px; }
  .box-consulting { left: 862px; top: 13px; width: 123px; height: 78px; }
  .box-managed { left: 1040px; top: 14px; width: 123px; height: 81px; }
  .capability-list {
    position: absolute; list-style: none; color: var(--ink); font-size: 20px;
  }
  .capability-list li { position: relative; height: 41px; padding-left: 32px; white-space: nowrap; }
  .capability-list li::before {
    content: ""; position: absolute; left: 3px; top: 10px;
    width: 5px; height: 5px; border-radius: 50%; background: var(--ink);
  }
  .list-left { left: 78px; top: 505px; }
  .list-right { left: 860px; top: 530px; }
</style>
</head>
<body>
<div class="slide">
  <div class="top-rule"></div>
  <div class="side-strip"></div>

  <svg class="network-art" width="1200" height="675" viewBox="0 0 1200 675" aria-hidden="true">
    <g fill="var(--hub-grey)">
      <circle cx="607" cy="316" r="236"/>
      <circle cx="607" cy="94" r="40"/>
      <circle cx="703.3" cy="116" r="40"/>
      <circle cx="780.6" cy="177.6" r="40"/>
      <circle cx="823.4" cy="266.6" r="40"/>
      <circle cx="823.4" cy="365.4" r="40"/>
      <circle cx="780.6" cy="454.4" r="40"/>
      <circle cx="703.3" cy="516" r="40"/>
      <circle cx="607" cy="538" r="40"/>
      <circle cx="510.7" cy="516" r="40"/>
      <circle cx="433.4" cy="454.4" r="40"/>
      <circle cx="390.6" cy="365.4" r="40"/>
      <circle cx="390.6" cy="266.6" r="40"/>
      <circle cx="433.4" cy="177.6" r="40"/>
      <circle cx="510.7" cy="116" r="40"/>
    </g>
    <g fill="none" stroke="var(--connector)" stroke-width="1">
      <polyline points="175,80 212,104 360,218"/>
      <polyline points="359,49 384,52 448,117"/>
      <polyline points="708,26 753,26 759,109"/>
      <polyline points="862,45 841,47 784,119"/>
      <polyline points="1040,80 1020,80 854,218"/>
    </g>
  </svg>

  <div class="hub-title">OAKVALE<br>EXECUTION<br>NETWORK</div>

  <div class="service-box box-operations">Restaurant<br>Manage<br>Operations</div>
  <div class="service-box box-technology">Technology<br>Services</div>
  <div class="service-box box-design">Design and Construction Services</div>
  <div class="service-box box-consulting">Strategic<br>Consulting<br>Services</div>
  <div class="service-box box-managed">IT Managed<br>Services</div>

  <ul class="capability-list list-left">
    <li>Expert Resources</li>
    <li>Product Sourcing</li>
    <li>Oakvale RMO</li>
  </ul>
  <ul class="capability-list list-right">
    <li>Restaurant Operations Team</li>
    <li>Nearshore Technology Center</li>
  </ul>

  <div class="footer-band">
    <span class="footer-date">4/7/2021</span>
    <span class="footer-url">www.oakvaleservices.com</span>
    <span class="footer-page">9</span>
  </div>
</div>
</body>
</html>
```